Postcard Design - Feb. 2014

We need a postcard design for a skin pathology laboratory in Long Beach, CA.( southern CA). We provide consultations on submitted specimens. Please see our website - www.skinslidereview.example. Our clients are other physicians. Modern, clean design is desired.
Updates

Reason: Considering current designs and anticipating more submissions. Thank you.

Target Market(s)

Dermatologists, other physicians.

Industry/Entity Type

Laboratory

Requirements
Must have
• Name of company: Harborview Cutaneous & Biopsy Associates, Inc.
Address: 4718 Marlow Crest Blvd. Suite 212, Long Beach, CA 90741.
Telephone # : 562 739 1046
website: www.skinslidereview.example
Information regarding teaching/educational section of website.
Nice to have
• Nice fonts.

```html
<!DOCTYPE html>
<html lang="en">
<head>
<meta charset="utf-8">
<title>Harborview Cutaneous &amp; Biopsy Associates – Postcard</title>
<link rel="stylesheet" href="https://fonts.googleapis.com/css2?family=Cabin:wght@400;500&family=Pathway+Gothic+One&display=swap">
<style>
  :root {
    --tissue-light: #cfc9cb;
    --tissue-mid: #a9a3a6;
    --tissue-dark: #6f6a6e;
    --skin-light: #f1d3c4;
    --skin-mid: #e0ad97;
    --ink: #1f1c1e;
    --white: #ffffff;
    --accent-red: #c8262b;
    --band: #121112;
    --band-text: #e8e6e6;
  }
  * { margin: 0; padding: 0; box-sizing: border-box; }
  html, body { width: 1200px; height: 800px; overflow: hidden; background: #e9e7e5; }
  .postcard {
    position: relative;
    width: 1200px;
    height: 800px;
    overflow: hidden;
    font-family: "Cabin", "Gill Sans", sans-serif;
    color: var(--ink);
  }
  .tissue-backdrop {
    position: absolute; inset: 0;
    background:
      radial-gradient(ellipse 60% 45% at 62% 34%, var(--tissue-dark) 0%, rgba(111,106,110,0) 70%),
      linear-gradient(160deg, var(--tissue-light) 0%, var(--tissue-mid) 45%, var(--tissue-light) 100%);
  }
  .company-rule {
    position: absolute; top: 84px; left: 0; right: 0;
    display: flex; align-items: center; justify-content: center; gap: 26px;
  }
  .company-rule .rule {
    flex: 1; height: 2px; background: var(--ink); position: relative;
  }
  .company-rule .rule.left { margin-left: 48px; }
  .company-rule .rule.right { margin-right: 48px; }
  .company-rule .rule.left::before,
  .company-rule .rule.right::after {
    content: ""; position: absolute; top: -4px; width: 10px; height: 10px;
    border-radius: 50%; background: var(--ink);
  }
  .company-rule .rule.left::before { left: -5px; }
  .company-rule .rule.right::after { right: -5px; }
  .company-name {
    font-size: 31px; font-weight: 500; letter-spacing: 1px; white-space: nowrap;
    transform: translateY(-8px);
  }
  .hand-figure {
    position: absolute; left: 60px; top: 165px; width: 140px; height: 551px;
    border-radius: 70px 70px 0 0;
    background: linear-gradient(180deg, var(--skin-light) 0%, var(--skin-mid) 100%);
  }
  .specimen-links { position: absolute; inset: 0; }
  .message {
    position: absolute; left: 560px; width: 620px; top: 190px;
    text-align: center;
  }
  .physician-name {
    color: var(--white); font-size: 38px; font-weight: 400; letter-spacing: 0.5px;
    margin-bottom: 48px;
  }
  .tagline {
    font-family: "Pathway Gothic One", "Arial Narrow", sans-serif;
    font-size: 36px; line-height: 48px; letter-spacing: 1.5px; text-transform: uppercase;
  }
  .new-flag {
    font-family: "Pathway Gothic One", "Arial Narrow", sans-serif;
    color: var(--accent-red); font-size: 64px; line-height: 1; margin-top: 30px;
  }
  .teaching-note {
    font-family: "Pathway Gothic One", "Arial Narrow", sans-serif;
    font-size: 40px; letter-spacing: 1px; line-height: 1.1; margin-top: 6px;
  }
  .website { color: var(--white); font-size: 26px; letter-spacing: 0.5px; margin-top: 2px; }
  .contact-band {
    position: absolute; left: 0; right: 0; bottom: 0; height: 84px;
    background: var(--band); color: var(--band-text);
    display: flex; align-items: center; justify-content: space-between;
    padding: 0 30px 0 48px; font-size: 22px; letter-spacing: 0.3px;
  }
</style>
</head>
<body>
<main class="postcard">
  <div class="tissue-backdrop" role="img" aria-label="Soft grey microscope photograph of skin tissue layers"></div>

  <header class="company-rule">
    <span class="rule left"></span>
    <h1 class="company-name">Harborview Cutaneous &amp; Biopsy Associates, Inc.</h1>
    <span class="rule right"></span>
  </header>

  <div class="hand-figure" role="img" aria-label="Photograph of a raised open hand seen from the side"></div>

  <svg class="specimen-links" width="1200" height="800" viewBox="0 0 1200 800" aria-hidden="false">
    <g stroke="#1f1c1e" stroke-width="2">
      <line x1="190" y1="270" x2="353" y2="270"/>
      <line x1="175" y1="404" x2="273" y2="404"/>
      <line x1="170" y1="559" x2="273" y2="559"/>
    </g>
    <g fill="#1f1c1e">
      <circle cx="190" cy="270" r="4"/>
      <circle cx="175" cy="404" r="4"/>
      <circle cx="170" cy="559" r="4"/>
    </g>
    <g stroke="#111" stroke-width="7">
      <circle cx="420" cy="270" r="67" fill="#8f8a8e" role="img" aria-label="Micrograph of a skin specimen, detail one"/>
      <circle cx="328" cy="404" r="55" fill="#9d989b" role="img" aria-label="Micrograph of a skin specimen, detail two"/>
      <circle cx="349" cy="559" r="76" fill="#b3adb0" role="img" aria-label="Micrograph of a skin specimen, detail three"/>
    </g>
  </svg>

  <section class="message">
    <h2 class="physician-name">Mara L. Oyelaran, M.D.</h2>
    <p class="tagline">Ready to support your practice<br>with excellent<br>dermatopathology consultations</p>
    <p class="new-flag">New!</p>
    <p class="teaching-note">Teaching section on website</p>
    <p class="website">www.skinslidereview.example</p>
  </section>

  <footer class="contact-band">
    <span class="phone">P: 800.615.2297</span>
    <span class="address">4718 Marlow Crest Blvd. Suite 212, Long Beach, CA 90741</span>
  </footer>
</main>
</body>
</html>
```